brightwave pools cards

i need to create a design to use on my business cards,brochures and as a letterhead. i am a new swimming pool renovation business named BRIGHTWAVE POOLS. I require a smart professional deign to reflect that my business is the best in the industry.
should include something like.... Brightwave Pools ABN - 57184620931
residential pool renovation specialists
specialising in the art of - fully tiled pools
- waterline tiles
- natural stone pool copings
and outdoor areas - concrete slabs - detailed mosaic work - pool lighting and water features - pool painting

trent - 0461829304 gordon -0438152967 brightwavepoolsnorth@mailbox-example.com

the design could feature - water, natural stone (travertine, sandstone etc), something to personafy the word imagine.
looking foward to seeing some ideas... cheers heaps trent

```html
<!DOCTYPE html>
<html lang="en">
<head>
<meta charset="utf-8">
<title>Brightwave Pools – Business Cards</title>
<link href="https://fonts.googleapis.com/css2?family=Oswald:wght@300;400&display=swap" rel="stylesheet">
<style>
  :root {
    --page: #ffffff;
    --tile-light: #bfe3f7;
    --tile-mid: #8ccaee;
    --tile-deep: #4d8fd6;
    --tile-navy: #2f5fb3;
    --panel: #b3dcf2;
    --ink: #2c56a8;
    --white: #ffffff;
  }
  * { margin: 0; padding: 0; box-sizing: border-box; }
  html, body {
    width: 800px; height: 1200px; overflow: hidden;
    background: var(--page);
    font-family: "Oswald", "Arial Narrow", sans-serif;
  }
  .canvas { position: relative; width: 800px; height: 1200px; }

  .card { position: absolute; left: 98px; width: 599px; height: 330px; overflow: hidden; }

  /* Front */
  .card--front { top: 10px; }
  .card--front .mosaic {
    position: absolute; inset: 0;
    background:
      radial-gradient(ellipse at 30% 35%, rgba(77,143,214,.45), transparent 60%),
      linear-gradient(180deg, var(--tile-mid) 0%, var(--tile-light) 45%, var(--tile-mid) 100%);
  }
  .front__name {
    position: absolute; left: 0; right: 0; top: 4px;
    text-align: center; color: var(--white);
    font-weight: 400; font-size: 104px; line-height: 104px;
    letter-spacing: -1px;
  }
  .front__tagline {
    position: absolute; left: 0; right: 0; top: 250px;
    text-align: center; color: var(--ink);
    font-weight: 400; font-size: 19px;
  }
  .front__contacts {
    position: absolute; left: 0; right: 0; top: 281px;
    text-align: center; color: var(--ink);
    font-weight: 300; font-size: 12.5px;
  }
  .front__contacts span + span { margin-left: 8px; }

  /* Back */
  .card--back { top: 375px; background: var(--panel); }
  .card--back .mosaic {
    position: absolute; left: 0; top: 0; width: 200px; height: 100%;
    background: linear-gradient(180deg, var(--tile-deep) 0%, var(--tile-mid) 35%, var(--tile-navy) 60%, var(--tile-mid) 100%);
  }
  .back__name {
    position: absolute; left: 207px; top: 18px;
    color: var(--white);
    font-weight: 400; font-size: 48px; line-height: 56px;
    letter-spacing: -0.5px;
    -webkit-text-stroke: 0;
  }
  .back__name { color: var(--white); }
  .back__details {
    position: absolute; left: 225px; top: 104px;
    color: var(--ink); list-style: none;
    font-weight: 300; font-size: 14px; line-height: 19.6px;
  }
</style>
</head>
<body>
<main class="canvas">

  <section class="card card--front">
    <div class="mosaic" role="img" aria-label="Blue pool mosaic tile background with a stepped darker tile line"></div>
    <h1 class="front__name">BRIGHTWAVE<br>POOLS</h1>
    <p class="front__tagline">Residential Pool Renovation Specialists</p>
    <p class="front__contacts">
      <span>Trent: 0461829304</span><span>Gordon: 0438152967</span><span>brightwavepoolsnorth@mailbox-example.com</span>
    </p>
  </section>

  <section class="card card--back">
    <div class="mosaic" role="img" aria-label="Strip of blue pool mosaic tiles"></div>
    <h2 class="back__name">BRIGHTWAVE POOLS</h2>
    <ul class="back__details">
      <li>ABN - 57184620931</li>
      <li>SPECIALISING IN THE ART OF:</li>
      <li>Fully tiled pools</li>
      <li>Waterline tiles</li>
      <li>Natural stone pool copings and outdoor areas</li>
      <li>Concrete slabs</li>
      <li>Detailed mosaic work</li>
      <li>Pool lighting and water features</li>
      <li>Pool painting</li>
    </ul>
  </section>

</main>
</body>
</html>
```